Bathroom Remodeling Guide Needed

We need to create a Bathroom remodeling guide that we can give away as a freemium download. The attached file contains the instructions and copy for the guide along with our logo. Below is a dropbox link to our assets folder as well.

https://www.filevantor.com/shr/fd/q7kzmwtrpl4bxe829hcvua/KTRmWqvbPzXc3hLyJuGaTo5?rkey=7hvbq2093kw8tf1ma5512d48x&dl=0

```html
<!DOCTYPE html>
<html lang="en">
<head>
<meta charset="utf-8">
<title>The Homeowner's Guide to Bathroom Remodeling in Charlotte</title>
<link href="https://fonts.googleapis.com/css2?family=Libre+Baskerville:ital@0;1&family=Lato:ital,wght@0,400;0,700;1,400&display=swap" rel="stylesheet">
<style>
  :root{
    --backdrop:#b5aca2;
    --page:#ffffff;
    --heading:#8a735a;
    --panel:#8b7259;
    --ink:#2b2724;
    --muted:#5a524b;
    --light:#f3eee8;
  }
  *{box-sizing:border-box;margin:0;padding:0}
  html,body{width:1200px;height:2640px;overflow:hidden;background:var(--backdrop)}
  .canvas{position:relative;width:1200px;height:2640px}
  .page{position:absolute;width:476px;height:367px;background:var(--page);overflow:hidden;box-shadow:0 6px 16px rgba(60,45,30,.18);font-family:"Lato",sans-serif;color:var(--ink)}
  .col-a{left:84px}.col-b{left:640px}
  .row-1{top:69px}.row-2{top:496px}.row-3{top:922px}.row-4{top:1350px}.row-5{top:1776px}.row-6{top:2203px}
  .photo{position:absolute}
  .title{position:absolute;font-family:"Libre Baskerville",serif;color:var(--heading);font-weight:400;line-height:1.12;font-size:20px}
  .body{position:absolute;font-size:7.4px;line-height:1.38;color:var(--ink)}
  .body p{margin-bottom:7px}
  .body ul{list-style:none;margin-bottom:7px}
  .body li::before{content:"• "}
  .brand{position:absolute;display:flex;align-items:center;gap:4px;font-family:"Lato",sans-serif;font-weight:700;font-size:8px;letter-spacing:.5px;color:var(--ink)}
  .brand .mark{width:8px;height:8px;border:1px solid var(--ink)}
  /* cover */
  .cover-kicker{font-style:italic;font-size:16px}
  .cover-main{font-size:29px;line-height:1.02}
  .cover-place{font-style:italic;font-size:16px}
  .cover-sub{position:absolute;left:16px;top:316px;font-size:7.4px;font-style:italic;line-height:1.4}
  /* process */
  .panel{position:absolute;left:0;top:94px}
  .process-intro{position:absolute;left:0;width:440px;top:135px;text-align:center;color:#fff;font-size:7.2px;line-height:1.4}
  .step{position:absolute;top:178px;width:78px;text-align:center;color:#fff}
  .step-num{font-family:"Libre Baskerville",serif;font-size:20px}
  .step-name{font-family:"Libre Baskerville",serif;font-size:9.5px;line-height:1.2;margin-top:12px;height:28px}
  .step-text{font-size:5.6px;font-style:italic;line-height:1.35;margin-top:6px;color:var(--light)}
  .arrow{position:absolute;top:186px;color:#fff;font-size:14px}
  .quote{font-style:italic}
  .cite{margin-top:2px}
</style>
</head>
<body>
<main class="canvas">

  <!-- Cover -->
  <section class="page col-a row-1">
    <div class="photo" role="img" aria-label="Bright modern bathroom with freestanding tub and light wood vanity" style="inset:0;clip-path:polygon(258px 88px,476px 88px,476px 367px,205px 367px);background:linear-gradient(180deg,#f6f4f1 0%,#e9e3dc 55%,#cdb79a 100%)"></div>
    <div class="brand" style="right:18px;top:22px"><span class="mark"></span>HEARTHLINE</div>
    <h1 class="title" style="left:16px;top:190px">
      <span class="cover-kicker">The Homeowner’s<br>Guide to</span><br>
      <span class="cover-main">Bathroom<br>Remodeling</span><br>
      <span class="cover-place">in Charlotte</span>
    </h1>
    <p class="cover-sub">How to Plan, Design, and Build a Bathroom<br>You’ll Love for Years to Come</p>
  </section>

  <!-- Before you start -->
  <section class="page col-b row-1">
    <div class="photo" role="img" aria-label="Clawfoot tub against white subway tile with rustic wood vanity" style="inset:0;clip-path:polygon(0 0,476px 0,476px 148px,420px 126px,0 165px);background:linear-gradient(90deg,#e7e4df 0%,#d9d3cb 55%,#8a6a4c 100%)"></div>
    <h2 class="title" style="left:22px;top:174px">Before You Start<br>Your Bathroom<br>Remodel</h2>
    <div class="body" style="left:208px;top:178px;width:245px">
      <p>Remodeling your bathroom is one of the most impactful upgrades you can make to your home. Done right, it improves how you start and end your day, increases your home’s value, and creates a space that feels both functional and refined.</p>
      <p>But without the right plan, it can quickly become overwhelming.</p>
      <p>Many homeowners begin with inspiration photos and good intentions, only to run into unexpected costs, delays, and decisions they weren’t prepared for.</p>
      <p>This guide was created to give you clarity before you begin—so you can move forward with confidence, avoid common mistakes, and ultimately achieve a result you’ll be proud of for years to come.</p>
    </div>
  </section>

  <!-- Go wrong -->
  <section class="page col-a row-2">
    <div class="photo" role="img" aria-label="White tiled shower with black fixtures and glass panel" style="inset:0;clip-path:polygon(0 0,175px 0,135px 367px,0 367px);background:linear-gradient(160deg,#ecebe8 0%,#c9c7c3 60%,#9d9a95 100%)"></div>
    <h2 class="title" style="left:193px;top:50px">Most Bathroom<br>Remodels Go Wrong<br>Before They Even Start</h2>
    <div class="body" style="left:193px;top:143px;width:250px">
      <p>The success of a bathroom remodel is determined long before construction begins.</p>
      <p>The most common mistake homeowners make is starting without a clear, well-thought-out plan. Decisions are made on the fly, materials are selected too late, and small issues quickly turn into costly problems.</p>
      <p>A successful project requires:</p>
      <ul><li>A clear design vision</li><li>Thoughtful material selection</li><li>Proper planning before demolition</li><li>A team that understands both design and construction</li></ul>
      <p>When these elements are in place, the process becomes smooth, predictable, and even enjoyable.</p>
      <p>When they’re not, the experience is often the opposite.</p>
    </div>
  </section>

  <!-- Costs -->
  <section class="page col-b row-2">
    <div class="photo" role="img" aria-label="Black framed mirror over white vessel sink with matte black faucet" style="inset:0;clip-path:polygon(296px 0,476px 0,476px 367px,294px 367px,330px 190px);background:linear-gradient(180deg,#e6e6e4 0%,#d5d5d2 60%,#2a2a2c 100%)"></div>
    <h2 class="title" style="left:25px;top:50px">Understanding Bathroom<br>Remodeling Costs</h2>
    <div class="body" style="left:25px;top:127px;width:250px">
      <p>Every bathroom remodel is unique, but most projects fall within a predictable range depending on size, scope, and finishes.</p>
      <p>At Hearthline Kitchen &amp; Bath, most bathroom remodeling projects start at $35,000 and increase based on complexity, materials, and customization.</p>
      <p style="margin-bottom:0">Several factors influence the total investment:</p>
      <ul><li>The size of the space</li><li>Tile selection and layout complexity</li><li>Plumbing or layout changes</li><li>Custom vanities and cabinetry</li><li>Lighting and fixture upgrades</li><li>Specialty features such as walk-in showers or freestanding tubs</li></ul>
      <p>Rather than focusing on the lowest possible cost, our approach is to deliver long-term value—combining thoughtful design, quality materials, and expert craftsmanship.</p>
    </div>
  </section>

  <!-- Design foundation -->
  <section class="page col-a row-3">
    <div class="photo" role="img" aria-label="Hands framing a bathroom half sketched and half finished" style="inset:0;clip-path:polygon(0 0,476px 0,476px 132px,445px 140px,0 178px);background:linear-gradient(90deg,#f1efec 0%,#ddd3c4 40%,#c8b89f 65%,#f1efec 100%)"></div>
    <h2 class="title" style="left:18px;top:182px">Why Design Is<br>the Foundation<br>of a Successful<br>Remodel?</h2>
    <div class="body" style="left:219px;top:182px;width:240px">
      <p>A beautiful bathroom doesn’t happen by accident—it is designed.</p>
      <p>Layout, lighting, storage, and material selection must all work together to create a space that feels cohesive and functions effortlessly.</p>
      <p>Every project we take on includes a professional designer at no additional cost. This ensures that your bathroom is carefully planned before construction begins, eliminating guesswork and reducing the likelihood of costly changes later.</p>
      <p>With a clear design in place, you’ll be able to visualize your new space, make confident decisions, and move into construction with clarity.</p>
    </div>
  </section>

  <!-- Process -->
  <section class="page col-b row-3">
    <h2 class="title" style="left:24px;top:22px">What to Expect When<br>You Work With Us</h2>
    <svg class="panel" width="476" height="250" viewBox="0 0 476 250" aria-hidden="true"><polygon points="0,0 440,0 461,208 440,248 0,248" fill="#8b7259"/></svg>
    <p class="process-intro">A structured process is what separates a stressful remodel from a smooth one.<br>Here’s how we guide you through each phase:</p>
    <div class="step" style="left:13px"><div class="step-num">1</div><div class="step-name">Consultation<br>&amp; Vision</div><div class="step-text">We begin by understanding your goals, your style, and how you want your space to function.</div></div>
    <span class="arrow" style="left:85px">→</span>
    <div class="step" style="left:97px"><div class="step-num">2</div><div class="step-name">Measurement<br>&amp; Design</div><div class="step-text">We take precise measurements and develop a professional design plan tailored to your space.</div></div>
    <span class="arrow" style="left:169px">→</span>
    <div class="step" style="left:181px"><div class="step-num">3</div><div class="step-name">Material<br>Selection</div><div class="step-text">We guide you through selecting materials, finishes, and fixtures that align with your vision and investment level.</div></div>
    <span class="arrow" style="left:253px">→</span>
    <div class="step" style="left:265px"><div class="step-num">4</div><div class="step-name">Construction</div><div class="step-text">Our team executes the project with attention to detail, cleanliness, and respect for your home.</div></div>
    <span class="arrow" style="left:337px">→</span>
    <div class="step" style="left:349px"><div class="step-num">5</div><div class="step-name">Final<br>Walkthrough</div><div class="step-text">We review every detail together to ensure everything meets our standards—and yours.</div></div>
  </section>

  <!-- Timeline -->
  <section class="page col-a row-4">
    <div class="photo" role="img" aria-label="Marble bathroom with navy vanity, freestanding tub and chandelier" style="inset:0;clip-path:polygon(0 0,310px 0,328px 367px,0 367px);background:linear-gradient(180deg,#eef0f1 0%,#dfe2e4 50%,#3d4657 80%,#e9e9e9 100%)"></div>
    <h2 class="title" style="left:339px;top:34px">How Long<br>Does a<br>Bathroom<br>Remodel<br>Take?</h2>
    <div class="body" style="left:339px;top:176px;width:120px">
      <p>One of the most common questions we hear is: “How long will this take?”</p>
      <p style="margin-bottom:0">While every project is different, most bathroom remodels take:</p>
      <ul><li>3–6 weeks during construction</li><li>6–10 weeks total including planning and design</li></ul>
      <p>The planning phase is critical. When decisions are made upfront, construction moves efficiently and delays are minimized.</p>
    </div>
  </section>

  <!-- Upgrades -->
  <section class="page col-b row-4">
    <h2 class="title" style="left:16px;top:20px">Popular<br>Upgrades<br>Homeowners<br>Love</h2>
    <div class="photo" role="img" aria-label="Luxury bathroom with marble wall, walnut slats and soaking tub" style="left:158px;top:98px;width:318px;height:241px;background:linear-gradient(90deg,#5a3d2a 0%,#c9bfb4 40%,#e4ded7 60%,#6b4a33 100%)"></div>
    <div class="body" style="left:16px;top:160px;width:130px">
      <p>Today’s bathrooms are designed to feel like personal retreats. Some of the most requested features include:</p>
      <ul><li>Walk-in showers with frameless glass</li><li>Floating or custom vanities</li><li>Heated tile flooring</li><li>Freestanding soaking tubs</li><li>LED backlit mirrors</li><li>Custom storage solutions</li></ul>
      <p>These features not only improve daily comfort but also add long-term value to your home.</p>
    </div>
  </section>

  <!-- Before/after -->
  <section class="page col-a row-5">
    <h2 class="title" style="left:28px;top:20px">From<br>Outdated to<br>Exceptional</h2>
    <div class="body" style="left:193px;top:32px;width:245px">
      <p>One of the most rewarding parts of what we do is transforming a space that no longer works into one that feels entirely new.</p>
      <p>Below is an example of a small bathroom renovation where we improved functionality, updated materials, and created a clean, modern design.</p>
    </div>
    <div class="photo" role="img" aria-label="Bathroom stripped to wood framing before renovation" style="left:20px;top:126px;width:194px;height:128px;background:linear-gradient(90deg,#8a5a30,#c89a62,#7a4e2a)"></div>
    <div class="photo" role="img" aria-label="Finished bathroom with navy double vanity and glass shower" style="left:262px;top:126px;width:195px;height:128px;background:linear-gradient(180deg,#d8dcdd,#a8b0b6 60%,#2e3a55)"></div>
    <div class="photo" role="img" aria-label="Plumbing and framing during construction" style="left:142px;top:222px;width:195px;height:128px;background:linear-gradient(135deg,#c4894f,#7a3b2e 50%,#b39a7a)"></div>
  </section>

  <!-- Partner -->
  <section class="page col-b row-5">
    <div class="photo" role="img" aria-label="Concrete-toned bathroom with round mirror, wood vanity and rain shower" style="left:0;top:86px;width:238px;height:263px;background:linear-gradient(180deg,#c9c4be 0%,#b7b1aa 60%,#8b6a4a 75%,#c1bcb6 100%)"></div>
    <h2 class="title" style="left:257px;top:88px">Choosing the<br>Right Remodeling<br>Partner</h2>
    <div class="body" style="left:257px;top:170px;width:205px">
      <p>The contractor you choose will ultimately determine your experience and your outcome.</p>
      <p style="margin-bottom:0">When evaluating a remodeling company, look for:</p>
      <ul><li>A clear and defined process</li><li>Strong communication from start to finish</li><li>Design capabilities—not just construction</li><li>Transparent and realistic pricing</li><li>A portfolio of completed projects</li><li>Positive client experiences and reviews</li></ul>
      <p>The right partner will make the process feel organized, predictable, and well-managed.</p>
    </div>
  </section>

  <!-- Testimonials -->
  <section class="page col-a row-6">
    <div class="photo" role="img" aria-label="Soft neutral bathroom corner with dried flowers" style="left:0;top:0;width:78px;height:367px;background:linear-gradient(180deg,#efe9e2,#d9c8b4 60%,#efeae4)"></div>
    <div class="photo" role="img" aria-label="Light wood vanity with round mirror" style="left:398px;top:0;width:78px;height:367px;background:linear-gradient(180deg,#ece6df,#c9ab86 65%,#e3d8cb)"></div>
    <h2 class="title" style="left:78px;width:320px;top:40px;text-align:center;font-size:21px">Client Experiences</h2>
    <div class="body" style="left:117px;top:108px;width:245px">
      <p class="quote">“Hearthline Kitchen And Bath just completed a two full bath and one powder room renovation for me. I cannot say enough good things about the team. Marcus Elling communicated throughout the process and checked on progress of the project throughout. His team and subcontractors all performed very well. They cleaned after themselves every day and took extra care of my home… I highly recommend Hearthline Kitchen And Bath.”<br>— Dana Whitfield, Charlotte NC</p>
      <p class="quote" style="margin-top:30px">“I can’t say enough about my experience with the team at Hearthline Kitchen &amp; Bath. Far different and BETTER than any other experience we have had with other contractors… They were transparent with pricing, stayed within budget, and even finished ahead of schedule.”<br>— Renee, Charlotte NC</p>
    </div>
  </section>

  <!-- Closing -->
  <section class="page col-b row-6">
    <div class="photo" role="img" aria-label="Walk-in glass shower beside warm wood floating vanity" style="inset:0;clip-path:polygon(0 0,318px 0,330px 367px,0 367px);background:linear-gradient(90deg,#cfcac4 0%,#b99067 45%,#d8d2cb 70%,#c4beb7 100%)"></div>
    <h2 class="title" style="left:338px;top:28px;font-size:21px">Let’s<br>Design<br>Your<br>Bathroom</h2>
    <div class="body" style="left:338px;top:142px;width:125px">
      <p>The best place to start is with a conversation.</p>
      <p>We’ll help you clarify your vision, explore your options, and create a plan tailored specifically to your home.</p>
      <p style="font-size:6px;margin-top:20px">Schedule Your Design<br>Consultation</p>
      <p style="font-size:6px">Hearthline Kitchen &amp; Bath<br>Charlotte, NC</p>
    </div>
    <div class="brand" style="left:372px;top:325px;font-size:9px"><span class="mark"></span>HEARTHLINE</div>
  </section>

</main>
</body>
</html>
```